New Label Design Project

We need to create a label for a new product that you spray onto your car to wax the vehicle after a wash. We have a very limited amount of time to create this label. How the Product Works: Spray onto your vehicle surface when its still wet, right after the rinse step of a Car Wash. You spray it on, and the Wax adheres on-contact in seconds. After you've sprayed the product on your car you rinse your vehicle and BAM your car is waxed.

```html
<!DOCTYPE html>
<html lang="en">
<head>
<meta charset="utf-8">
<title>Spray Wax Label</title>
<link rel="stylesheet" href="https://fonts.googleapis.com/css2?family=Poppins:ital,wght@0,400;0,600;0,700;1,800;1,900&display=swap">
<style>
  :root {
    --page-bg: #c8cbd0;
    --label-black: #121212;
    --label-charcoal: #202226;
    --brand-blue: #0a7cf5;
    --deep-blue: #0552b8;
    --light-blue: #4aa3ff;
    --silver-light: #f2f2f2;
    --silver-dark: #8e8e8e;
    --white: #ffffff;
    --rule-grey: #6b6b6b;
  }
  * { margin: 0; padding: 0; box-sizing: border-box; }
  html, body {
    width: 1151px;
    height: 1200px;
    overflow: hidden;
    background: var(--page-bg);
    font-family: "Poppins", sans-serif;
  }
  .label {
    position: absolute;
    left: 268px;
    top: 20px;
    width: 614px;
    height: 1160px;
    display: block;
  }
  .logo-word { font-family: "Poppins", sans-serif; font-weight: 700; font-size: 72px; fill: var(--white); }
  .product-word { font-family: "Poppins", sans-serif; font-weight: 900; font-style: italic; font-size: 128px; }
  .feature-ring { fill: none; stroke: var(--brand-blue); stroke-width: 3; }
  .feature-label { font-family: "Poppins", sans-serif; font-weight: 700; font-size: 14px; fill: var(--white); }
  .tagline { font-family: "Poppins", sans-serif; font-weight: 600; font-size: 27px; fill: var(--white); }
  .body-copy { font-family: "Poppins", sans-serif; font-weight: 400; font-size: 14.5px; fill: var(--white); }
  .volume { font-family: "Poppins", sans-serif; font-weight: 700; font-size: 31px; fill: var(--white); }
  .divider { stroke: var(--rule-grey); stroke-width: 1.2; }
</style>
</head>
<body>
<svg class="label" viewBox="0 0 614 1160" xmlns="http://www.w3.org/2000/svg">
  <defs>
    <radialGradient id="panelGlow" cx="50%" cy="45%" r="70%">
      <stop offset="0" stop-color="#26282c"/>
      <stop offset="1" stop-color="#111111"/>
    </radialGradient>
    <linearGradient id="titleFill" x1="0" y1="0" x2="1" y2="0">
      <stop offset="0" stop-color="#1a8cff"/>
      <stop offset="0.5" stop-color="#0a6de0"/>
      <stop offset="1" stop-color="#0552b8"/>
    </linearGradient>
    <linearGradient id="silverStripe" x1="0" y1="0" x2="1" y2="0">
      <stop offset="0" stop-color="#ffffff"/>
      <stop offset="0.6" stop-color="#e4e4e4"/>
      <stop offset="1" stop-color="#8e8e8e"/>
    </linearGradient>
  </defs>

  <!-- panel -->
  <rect class="label-panel" x="0" y="0" width="614" height="1160" fill="url(#panelGlow)"/>
  <rect class="texture-area" x="0" y="40" width="614" height="1040" fill="url(#panelGlow)" opacity="0.6"
        role="img" aria-label="Subtle dark hexagon mesh texture"/>

  <!-- top band -->
  <rect class="top-band" x="0" y="0" width="614" height="40" fill="var(--brand-blue)"/>

  <!-- brand -->
  <text class="logo-word" x="309" y="157" text-anchor="middle">LOGO</text>

  <!-- product name, vertical -->
  <text class="product-word" transform="translate(212 1062) rotate(-90)" textLength="877" lengthAdjust="spacingAndGlyphs"
        fill="url(#titleFill)" stroke="#d8d8d8" stroke-width="2">PRODUCT</text>
  <text class="product-word" transform="translate(318 803) rotate(-90)" textLength="541" lengthAdjust="spacingAndGlyphs"
        fill="url(#titleFill)" stroke="#9a9a9a" stroke-width="2">NAME</text>

  <!-- feature badges -->
  <g class="feature feature-vinyl">
    <circle class="feature-ring" cx="457" cy="378" r="67"/>
    <rect x="441" y="340" width="32" height="38" rx="6" fill="var(--brand-blue)" role="img" aria-label="Car seat icon"/>
    <text class="feature-label" x="457" y="410" text-anchor="middle">VINYL</text>
  </g>
  <g class="feature feature-rubber">
    <circle class="feature-ring" cx="457" cy="560" r="67"/>
    <rect x="440" y="528" width="34" height="28" rx="3" fill="var(--brand-blue)" role="img" aria-label="Rubber trim icon"/>
    <text class="feature-label" x="457" y="577" text-anchor="middle">RUBBER</text>
  </g>
  <g class="feature feature-exterior">
    <circle class="feature-ring" cx="457" cy="731" r="67"/>
    <rect x="427" y="697" width="26" height="38" rx="2" fill="var(--brand-blue)"/>
    <rect x="461" y="697" width="26" height="38" rx="2" fill="var(--brand-blue)"/>
    <rect x="455.5" y="692" width="3" height="48" fill="var(--brand-blue)"/>
    <path d="M443 709 l-6 7 6 7" fill="none" stroke="var(--label-black)" stroke-width="2.5"/>
    <path d="M471 709 l6 7 -6 7" fill="none" stroke="var(--label-black)" stroke-width="2.5"/>
    <text class="feature-label" x="457" y="765" text-anchor="middle">EXTERIOR</text>
  </g>

  <!-- copy -->
  <text class="tagline" x="231" y="860">Lorem ipsum dolor sit</text>
  <text class="tagline" x="231" y="887">amet, consectetur</text>
  <line class="divider" x1="231" y1="925" x2="504" y2="925"/>
  <text class="body-copy" x="231" y="965" textLength="305" lengthAdjust="spacing">Lorem ipsum dolor sit amet, consectetur</text>
  <text class="body-copy" x="231" y="983">adipiscing elit, sed do</text>
  <line class="divider" x1="231" y1="1009" x2="504" y2="1009"/>
  <text class="volume" x="231" y="1065">500ml</text>

  <!-- bottom bands -->
  <rect class="silver-stripe" x="0" y="1082" width="614" height="14" fill="url(#silverStripe)"/>
  <rect class="bottom-band" x="0" y="1106" width="614" height="54" fill="var(--brand-blue)"/>
</svg>
</body>
</html>
```